K.R.O.U.B.S. Content Framework Infographic

I am looking to take my basic infographic to the next level. I need to to translate the content marketing concept that is outlined in the uploaded file. I have attached the content and the image I would like used. I am not stuck on the colors represented in the image but do want to see a variety of options.

Target Market(s)

Companies that are looking for a content marketing strategy, SEO Agencies, marketing agencies

Industry/Entity Type

Digital marketing, SEO

Font styles to use
Other font styles liked:
• arial, calibri are fine

Colors
0054AA
0677BA
7BADD7
CADEEF
E8F1F8
0094D4
00A9DD
6FCCEA
C7EBF8
E9F6FB
00AB8E
00BBA5
67D7C9
C6EFE9
E9F9F6
59FF00
82FF00
B8FF75
E3FFCB
F4FFEA
EE7325
F08F49
F5BC92
FAE3D3
FDF4ED
EB3D1F
EC4F4E
F09395
F8D3D4
FCEDEE

Requirements
Must have
• The image that I provided with the content breakdown with section connectors to the image
Nice to have
• a few different way to present the data

```html
<!DOCTYPE html>
<html lang="en">
<head>
<meta charset="utf-8">
<title>K.R.O.U.B.S. Content Framework Infographic</title>
<link rel="stylesheet" href="https://fonts.googleapis.com/css2?family=Archivo+Black&family=Barlow+Condensed:wght@400;500;600;700&display=swap">
<style>
  :root{
    --salmon:#f07c75;
    --charcoal:#5e5e5e;
    --sidebar:#f2eeee;
    --peach:#f9bb9c;
    --rose:#f1908a;
    --coral:#ec5552;
    --amber:#e1845c;
    --crimson:#cc1b3c;
    --wine:#8d1c3b;
    --ink:#3c3c3c;
    --backdrop:#e4e4e4;
    --white:#ffffff;
  }
  *{box-sizing:border-box;margin:0;padding:0}
  html,body{width:1200px;height:1200px;overflow:hidden;background:var(--backdrop)}
  body{position:relative;font-family:"Barlow Condensed",Arial,sans-serif;color:var(--ink)}
  .poster{position:absolute;left:0;top:136px;width:1200px;height:927px;background:var(--white);overflow:hidden}

  .masthead{position:absolute;left:0;top:0;width:1200px;height:146px;background:var(--salmon);text-align:center;padding-top:20px}
  .masthead h1{font-family:"Archivo Black",Arial,sans-serif;font-weight:400;color:var(--white);font-size:39px;line-height:46px;letter-spacing:1px;text-shadow:2px 2px 0 rgba(120,40,40,.35)}
  .intro-band{position:absolute;left:0;top:146px;width:1200px;height:92px;background:var(--charcoal)}
  .tagline{position:absolute;left:301px;top:127px;width:583px;height:38px;border-radius:19px;background:var(--white);text-align:center;font-family:"Archivo Black",Arial,sans-serif;font-size:25px;line-height:38px;color:var(--charcoal);letter-spacing:.5px}
  .tagline strong{color:var(--coral);font-weight:400}
  .intro-text{position:absolute;left:100px;top:176px;width:1000px;text-align:center;color:var(--white);font-family:"Barlow Condensed",Arial,sans-serif;font-weight:500;font-size:20px;line-height:26px}

  .sidebar{position:absolute;left:0;top:238px;width:272px;height:689px;background:var(--sidebar)}
  .sidebar h2{position:absolute;left:28px;top:34px;font-family:"Archivo Black",Arial,sans-serif;font-weight:400;font-size:38px;color:var(--coral);letter-spacing:1px}
  .sidebar h2::after{content:"";position:absolute;left:0;right:0;bottom:-6px;height:3px;background:var(--coral)}
  .pillar{position:absolute;left:24px;display:flex;align-items:center;gap:18px}
  .pillar .letter{width:68px;height:68px;border-radius:50%;display:flex;align-items:center;justify-content:center;color:var(--white);font-family:"Archivo Black",Arial,sans-serif;font-size:34px}
  .pillar .name{font-weight:700;font-size:24px;color:var(--charcoal);letter-spacing:.5px}
  .footer-url{position:absolute;left:0;bottom:0;width:272px;height:50px;background:var(--charcoal);color:var(--white);font-family:"Barlow Condensed",Arial,sans-serif;font-weight:700;font-size:20px;line-height:50px;padding-left:50px}

  .card{position:absolute;background:var(--white);border:1.5px solid;padding:7px 7px 9px;text-align:center;font-size:14px;line-height:17.5px;color:var(--ink)}
  .card h3{font-weight:700;font-size:18px;color:var(--white);letter-spacing:.5px;padding:2px 0;margin-bottom:7px}
  .card p{padding:0 4px}
  .card b{font-weight:700}

  .expertise{left:500px;top:267px;width:239px;min-height:160px;border-color:var(--rose)}
  .expertise h3{background:var(--rose)} .expertise b{color:var(--rose)}
  .engagement{left:756px;top:267px;width:232px;min-height:146px;border-color:var(--crimson)}
  .engagement h3{background:var(--crimson)} .engagement b{color:var(--crimson)}
  .multimedia{left:323px;top:471px;width:158px;min-height:235px;border-color:var(--peach)}
  .multimedia h3{background:var(--peach)} .multimedia b{color:var(--amber)}
  .trust{left:1005px;top:471px;width:162px;min-height:235px;border-color:var(--wine)}
  .trust h3{background:var(--wine)} .trust b{color:var(--wine)}
  .experience{left:505px;top:747px;width:235px;min-height:157px;border-color:var(--coral)}
  .experience h3{background:var(--coral)} .experience b{color:var(--coral)}
  .authority{left:753px;top:747px;width:235px;min-height:157px;border-color:var(--amber)}
  .authority h3{background:var(--amber)} .authority b{color:var(--amber)}

  .badge{position:absolute;width:90px;height:90px;border-radius:50%;display:flex;align-items:center;justify-content:center}
  .badge svg{width:48px;height:48px}

  .hero-figure{position:absolute;left:509px;top:453px;width:481px;height:252px;border-radius:120px 140px 60px 60px;background:linear-gradient(90deg,#f9bb9c 0%,#ec5552 40%,#cc1b3c 65%,#8d1c3b 100%)}
</style>
</head>
<body>
<main class="poster">
  <header class="masthead">
    <h1>PUTTING K.R.O.U.B.S. ON THE BONE<br>FOR THE USER &amp; SEARCHLY TO CHEW ON</h1>
  </header>
  <div class="intro-band"></div>
  <div class="tagline">IN SEO <strong>CONTENT</strong> IS STILL KING</div>
  <p class="intro-text">What has changed with content is not the content but the delivery of that content.&nbsp; People these days are consuming<br>content in so many different places &amp; formats that it makes it difficult to create engaging content that ranks and converts.</p>

  <aside class="sidebar">
    <h2>CONTENT</h2>
    <div class="pillar" style="top:107px"><span class="letter" style="background:var(--peach)">M</span><span class="name">MULTIMEDIA</span></div>
    <div class="pillar" style="top:192px"><span class="letter" style="background:var(--rose)">E</span><span class="name">EXPERTISE</span></div>
    <div class="pillar" style="top:273px"><span class="letter" style="background:var(--coral)">E</span><span class="name">EXPERIENCE</span></div>
    <div class="pillar" style="top:362px"><span class="letter" style="background:var(--amber)">E</span><span class="name">ENGAGEMENT</span></div>
    <div class="pillar" style="top:450px"><span class="letter" style="background:var(--crimson)">A</span><span class="name">AUTHORITY</span></div>
    <div class="pillar" style="top:539px"><span class="letter" style="background:var(--wine)">T</span><span class="name">TRUST</span></div>
    <div class="footer-url">WWW.WEBSITE.COM</div>
  </aside>

  <div class="hero-figure" role="img" aria-label="Illustrated pig divided into butcher-style cuts labelled Multimedia, Expertise, Experience, Engagement, Authority and Trust"></div>

  <section class="card expertise">
    <h3>EXPERTISE</h3>
    <p>refers to the content writer's level of knowledge or skill in a specific subject area that's relevant to the user's search query. <b>High-quality content</b> should be created by someone with relevant expertise in the topic being discussed.</p>
  </section>
  <section class="card engagement">
    <h3>ENGAGEMENT</h3>
    <p>is essential for views &amp; conversion as it keeps readers <b>locked in on content</b> to the point that they are more likely to move through the website experience and at least consider the value offered in the time that follow their website visit.</p>
  </section>
  <section class="card multimedia">
    <h3>MULTIMEDIA</h3>
    <p>consists of infographics, specific images, embedded videos, and other types content aside from the written word. <b>Highly engaging</b> as it presents desired information in a multifaceted but direct and timely manner.</p>
  </section>
  <section class="card trust">
    <h3>TRUST</h3>
    <p>is the <b>final result</b> of doing all of the above. If you can gain the user's trust about your content, Searchly and other search engines will "Trust" you and will provide you with the organic visibility we all strive for..</p>
  </section>
  <section class="card experience">
    <h3>EXPERIENCE</h3>
    <p>means that Searchly values firsthand or life experience of the author on the topic a page is about. It is important because often searchers want to know <b>first-hand information</b> before they decide to purchase something or use a certain service.</p>
  </section>
  <section class="card authority">
    <h3>AUTHORITY</h3>
    <p>the <b>credibility</b> of the content and the website it is hosted on. Authoritativeness can be established through the quality of the content, the site's reputation, author's reputation, external links &amp; content citations, and the credentials ofthe content creator.</p>
  </section>

  <div class="badge" style="left:415px;top:317px;background:var(--rose)">
    <svg viewBox="0 0 48 48" fill="#fff"><circle cx="24" cy="15" r="8"/><path d="M10 36c0-8 6-13 14-13s14 5 14 13z"/><circle cx="12" cy="42" r="2.5"/><circle cx="20" cy="43" r="2.5"/><circle cx="28" cy="43" r="2.5"/><circle cx="36" cy="42" r="2.5"/></svg>
  </div>
  <div class="badge" style="left:990px;top:330px;background:var(--crimson)">
    <svg viewBox="0 0 48 48" fill="none" stroke="#fff" stroke-width="2.5"><path d="M6 24c5-8 11-12 18-12s13 4 18 12c-5 8-11 12-18 12S11 32 6 24z"/><circle cx="24" cy="24" r="6"/><path d="M4 12V4h8M36 4h8v8M44 36v8h-8M12 44H4v-8"/></svg>
  </div>
  <div class="badge" style="left:357px;top:710px;background:var(--peach)">
    <svg viewBox="0 0 48 48" fill="none" stroke="#fff" stroke-width="2.5"><rect x="7" y="9" width="34" height="30" rx="2"/><path d="M7 35l10-11 8 8 5-5 11 10" fill="#fff"/><circle cx="31" cy="18" r="3.5" fill="#fff"/></svg>
  </div>
  <div class="badge" style="left:1042px;top:710px;background:var(--wine)">
    <svg viewBox="0 0 48 48" fill="#fff"><path d="M24 24c-6-5-10-8-10-12a5 5 0 0 1 10-1 5 5 0 0 1 10 1c0 4-4 7-10 12z"/><path d="M4 32h8l8 3h9a2 2 0 0 1 0 4h-8v1h10l10-6a2.5 2.5 0 0 1 3 4L32 44H12l-8-3z"/></svg>
  </div>
  <div class="badge" style="left:410px;top:801px;background:var(--coral)">
    <svg viewBox="0 0 48 48" fill="none" stroke="#fff" stroke-width="2.5"><path d="M14 42v-8c-5-3-8-8-8-14C6 11 14 5 23 5c9 0 16 6 16 15l4 8h-4v6c0 3-2 5-5 5h-5v3"/><circle cx="23" cy="19" r="5"/><path d="M23 10v3M23 25v3M14 19h3M29 19h3"/></svg>
  </div>
  <div class="badge" style="left:995px;top:808px;background:var(--amber)">
    <svg viewBox="0 0 48 48" fill="none" stroke="#fff" stroke-width="3"><path d="M36 24v16H8V12h20"/><path d="M16 24l7 7 17-19"/></svg>
  </div>
</main>
</body>
</html>
```